Project VELI

I am setting up a consultancy company in Istanbul, Turkey called VELI Partners. VELI partners will focus areas are highlighted in the attached presenatation. Expertise area as follows; Corporate Communications, Digitilization and Technology Integration, CSR & Sponsorships, Investor Relations and Fİnancial PR, Strategic Transactions, Corporate Governance... In related arease Project Management and Training support given.. For details see presenations. Our company collars are marun and blue.. In the attached presenations you can also see the business card colars and logo design. The design should reflect innovationi technology knowhow and power of communications skills. Enclosed you can find a presentations of scope of consultancy services and corporate logo from which logo and colars can be adapted..

Target Market(s)

Potential clients are any Holding or Company that would need services defined in the presantation attached.

Industry/Entity Type

It Company

Coding

Coded - Design and coding required

Number of Pages Required

5+ page

Font styles to use
Sans Serif

Requirements
Must have
• Main Expertize areas are defined in the presentation. The clients should be able to clearly see these and as they select the related area go to related page to see the content detail. I should be to also include vision statement in front page.. I should be able to present partners of the company in a related section. site should allow posting of pictures and an introductory video... Please use the logo and colars ı provided on attached file. Marun should be the dominating colar.
Nice to have
• www.morvanthrel.com I like.. Morvant provides somewhat similar services world wide. You can check out the site but don't need to necessarly do the same..

```html
<!DOCTYPE html>
<html lang="en">
<head>
<meta charset="utf-8">
<title>VELI Partners</title>
<link href="https://fonts.googleapis.com/css2?family=Source+Sans+3:wght@300;400;600;700&display=swap" rel="stylesheet">
<style>
  :root {
    --maroon: #650a4a;
    --blue: #2b2a93;
    --navy-deep: #1a0f4d;
    --navy: #232a7a;
    --hero-a: #2a1d78;
    --hero-b: #180b48;
    --card-bg: #f1f1f1;
    --text: #3a3a3a;
    --muted: #6b6b6b;
    --rule: #dddddd;
    --white: #ffffff;
    --footer: #1d1c5e;
    --footer-side: #25286a;
    --footer-link: #e6e6f5;
    --footer-head: #b9b9d6;
  }
  html, body { margin: 0; padding: 0; overflow: hidden; }
  body { font-family: "Source Sans 3", sans-serif; color: var(--text); background: var(--white); }
  .page { position: relative; width: 1200px; height: 2500px; overflow: hidden; background: var(--white); }
  .abs { position: absolute; }

  /* Header */
  .contact { right: 67px; top: 18px; text-align: right; color: var(--blue); font-size: 15px; line-height: 20px; }
  .brand { left: 53px; top: 66px; display: flex; align-items: center; gap: 10px; }
  .brand-dot { width: 14px; height: 14px; border-radius: 50%; background: var(--maroon); }
  .brand-name { font-size: 40px; font-weight: 700; color: var(--blue); letter-spacing: 1px; line-height: 44px; }
  .nav { right: 63px; top: 70px; display: flex; gap: 0; margin: 0; padding: 0; list-style: none; }
  .nav li { font-size: 13px; font-weight: 700; color: var(--blue); padding: 0 10px; height: 34px; line-height: 34px; text-transform: uppercase; }
  .nav li.active { background: var(--maroon); color: var(--white); }

  /* Hero */
  .hero { left: 0; top: 117px; width: 1200px; height: 541px;
    background: radial-gradient(ellipse at 20% 30%, #3b4ab0 0%, rgba(59,74,176,0) 45%),
                linear-gradient(100deg, var(--hero-a) 0%, #23197a 45%, var(--hero-b) 100%); }
  .hero-photo { left: 53px; top: 83px; width: 510px; height: 338px;
    background: linear-gradient(135deg, #8a6a4e 0%, #5a4a40 45%, #2c2b30 100%); }
  .hero-title { left: 610px; top: 130px; width: 540px; margin: 0; color: var(--white); font-size: 36px; font-weight: 700; line-height: 46px; }
  .hero-sub { left: 613px; top: 235px; width: 520px; margin: 0; color: var(--white); font-size: 26px; font-weight: 300; line-height: 34px; }
  .hero-btn { left: 613px; top: 328px; width: 174px; height: 47px; background: var(--white); color: var(--maroon); font-size: 26px; font-weight: 400; text-align: center; line-height: 46px; }
  .hero-dots { left: 1056px; top: 412px; display: flex; gap: 4px; }
  .hero-dots span { width: 9px; height: 9px; border-radius: 50%; background: #9a98c6; }
  .hero-dots span.on { background: var(--white); }
  .hero-tagline { left: 0; top: 462px; width: 1200px; margin: 0; text-align: center; color: var(--white); font-size: 28px; font-weight: 300; }

  /* Section titles */
  .section-title { left: 53px; width: 1084px; display: flex; align-items: center; gap: 22px; margin: 0; }
  .section-title::before, .section-title::after { content: ""; flex: 1; height: 1px; background: var(--rule); }
  .section-title span { font-size: 40px; font-weight: 300; color: #333; }
  .about-intro { left: 200px; top: 756px; width: 800px; margin: 0; text-align: center; color: var(--muted); font-size: 20px; font-weight: 300; line-height: 26px; }

  /* Service cards */
  .card { width: 340px; height: 455px; background: var(--card-bg); }
  .card h3 { position: absolute; left: 20px; top: 20px; margin: 0; font-size: 22px; font-weight: 400; color: var(--blue); line-height: 27px; }
  .card .media { position: absolute; left: 0; top: 88px; width: 340px; height: 144px; }
  .card p { position: absolute; left: 20px; top: 250px; width: 290px; margin: 0; font-size: 13px; line-height: 17px; color: var(--text); }
  .card .more { position: absolute; right: 0; bottom: 0; width: 52px; height: 20px; background: var(--maroon); color: var(--white); font-size: 11px; text-align: center; line-height: 20px; }
  .tone-office { background: linear-gradient(135deg, #6d7a88, #3b4048 60%, #22252a); }
  .tone-tech { background: linear-gradient(135deg, #2f3236, #5a5f66 60%, #9aa0a8); }
  .tone-hands { background: linear-gradient(135deg, #cfd9e6, #9fb0c7 50%, #3a4c6e); }
  .tone-paper { background: linear-gradient(135deg, #2a2a2c, #7a7670 55%, #e6e4e0); }
  .tone-laptop { background: linear-gradient(135deg, #f2f2f2, #c9cbcf 55%, #8b8f96); }
  .tone-meeting { background: linear-gradient(135deg, #e9e8e6, #a09a94 55%, #3a3a3e); }

  /* Press */
  .press { width: 520px; height: 143px; }
  .press .thumb { position: absolute; left: 0; top: 0; width: 157px; height: 143px; }
  .press h4 { position: absolute; left: 185px; top: 10px; margin: 0; font-size: 23px; font-weight: 400; color: #222; }
  .press p { position: absolute; left: 185px; top: 48px; width: 260px; margin: 0; font-size: 13px; line-height: 17px; color: var(--text); }
  .tone-tower { background: linear-gradient(160deg, #d8dde4, #7a8593 55%, #2e3440); }

  /* Footer */
  .footer { left: 0; top: 2167px; width: 1200px; height: 333px;
    background: linear-gradient(120deg, #1f3a8a 0%, var(--footer) 35%, var(--navy-deep) 100%); }
  .footer-side { left: 832px; top: 0; width: 368px; height: 333px; background: var(--footer-side); opacity: .85; }
  .footer-brand { left: 55px; top: 36px; display: flex; align-items: center; gap: 8px; }
  .footer-brand .brand-dot { background: var(--white); width: 12px; height: 12px; }
  .footer-brand .brand-name { color: var(--white); font-size: 36px; }
  .fcol h5 { margin: 0 0 10px; font-size: 13px; font-weight: 400; color: var(--footer-head); text-transform: uppercase; }
  .fcol ul { margin: 0; padding: 0; list-style: none; }
  .fcol li { font-size: 12px; line-height: 20px; color: var(--footer-link); }
  .subscribe { left: 872px; top: 40px; }
  .subscribe h5 { margin: 0 0 10px; font-size: 13px; font-weight: 400; color: var(--footer-head); text-transform: uppercase; }
  .sub-form { display: flex; }
  .sub-input { width: 167px; height: 32px; background: #8e8fb0; color: var(--white); font-size: 12px; line-height: 32px; padding-left: 20px; }
  .sub-btn { width: 92px; height: 32px; background: var(--maroon); color: var(--white); font-size: 12px; text-align: center; line-height: 32px; }
  .socials { display: flex; gap: 8px; margin-top: 22px; }
  .socials span { width: 24px; height: 24px; border-radius: 50%; background: var(--white); }
  .footer-rule { left: 53px; top: 285px; width: 1094px; height: 1px; background: rgba(255,255,255,.2); }
  .copyright { left: 55px; top: 300px; font-size: 12px; color: var(--footer-link); }
  .legal { right: 53px; top: 300px; display: flex; gap: 18px; font-size: 12px; color: var(--footer-link); }
</style>
</head>
<body>
<div class="page">

  <header>
    <div class="abs contact">sales@velipartners.com<br>1-555-014-2290</div>
    <div class="abs brand"><span class="brand-dot"></span><span class="brand-name">VELI</span></div>
    <ul class="abs nav">
      <li class="active">Who We Are</li>
      <li>What We Do</li>
      <li>Insights</li>
      <li>Global Network</li>
      <li>Careers &amp; Culture</li>
    </ul>
  </header>

  <section class="abs hero">
    <div class="abs hero-photo" role="img" aria-label="Portrait of a smiling businesswoman in a dark suit, colleagues blurred in an office behind her"></div>
    <h1 class="abs hero-title">Lorem Ipsum is simply dummy text of the printing</h1>
    <p class="abs hero-sub">Lorem Ipsum is simply dummy text<br>of the printing and typesetting industry.</p>
    <div class="abs hero-btn">Learn More</div>
    <div class="abs hero-dots"><span class="on"></span><span></span><span></span><span></span><span></span></div>
    <p class="abs hero-tagline">Lorem Ipsum is simply dummy text of the printing and typesetting industry.</p>
  </section>

  <h2 class="abs section-title" style="top:690px"><span>About VELI Partners.</span></h2>
  <p class="abs about-intro">Lorem Ipsum is simply dummy text of the printing and typesetting industry. Lorem Ipsum has been the industry's standard dummy text ever since the 1500</p>

  <article class="abs card" style="left:53px;top:835px">
    <h3>Corporate<br>Communications</h3>
    <div class="media tone-office" role="img" aria-label="Business team meeting around a table in an office"></div>
    <p>Lorem Ipsum is simply dummy text of the printing and typesetting industry. Lorem Ipsum has been the industry's standard dummy text ever since the 1500 Lorem Ipsum is simply dummy text of the printing and typesetting industry. Lorem Ipsum has been the industry's standard dummy text ever since the 1500 and typesetting industry.</p>
    <div class="more">more...</div>
  </article>
  <article class="abs card" style="left:425px;top:835px">
    <h3>Digitilization &amp;<br>Technology Integration</h3>
    <div class="media tone-tech" role="img" aria-label="Businessman touching a sketched diagram of technology ideas"></div>
    <p>Lorem Ipsum is simply dummy text of the printing and typesetting industry. Lorem Ipsum has been the industry's standard dummy text ever since the 1500 Lorem Ipsum is simply dummy text of the printing and typesetting industry. Lorem Ipsum has been the industry's standard dummy text ever since the 1500 and typesetting industry.</p>
    <div class="more">more...</div>
  </article>
  <article class="abs card" style="left:797px;top:835px">
    <h3>CSR &amp; Sponsorships</h3>
    <div class="media tone-hands" role="img" aria-label="Two business people shaking hands"></div>
    <p>Lorem Ipsum is simply dummy text of the printing and typesetting industry. Lorem Ipsum has been the industry's standard dummy text ever since the 1500 Lorem Ipsum is simply dummy text of the printing and typesetting industry. Lorem Ipsum has been the industry's standard dummy text ever since the 1500 and typesetting industry.</p>
    <div class="more">more...</div>
  </article>

  <article class="abs card" style="left:53px;top:1327px">
    <h3>Investor Relations &amp;<br>Financial PR</h3>
    <div class="media tone-paper" role="img" aria-label="Hands passing a document to be signed"></div>
    <p>Lorem Ipsum is simply dummy text of the printing and typesetting industry. Lorem Ipsum has been the industry's standard dummy text ever since the 1500 Lorem Ipsum is simply dummy text of the printing and typesetting industry. Lorem Ipsum has been the industry's standard dummy text ever since the 1500 and typesetting industry.</p>
    <div class="more">more...</div>
  </article>
  <article class="abs card" style="left:425px;top:1327px">
    <h3>Strategic Transactions</h3>
    <div class="media tone-laptop" role="img" aria-label="Hands typing on a laptop keyboard"></div>
    <p>Lorem Ipsum is simply dummy text of the printing and typesetting industry. Lorem Ipsum has been the industry's standard dummy text ever since the 1500 Lorem Ipsum is simply dummy text of the printing and typesetting industry. Lorem Ipsum has been the industry's standard dummy text ever since the 1500 and typesetting industry.</p>
    <div class="more">more...</div>
  </article>
  <article class="abs card" style="left:797px;top:1327px">
    <h3>Corporate Governance</h3>
    <div class="media tone-meeting" role="img" aria-label="Two colleagues reviewing work together at a desk"></div>
    <p>Lorem Ipsum is simply dummy text of the printing and typesetting industry. Lorem Ipsum has been the industry's standard dummy text ever since the 1500 Lorem Ipsum is simply dummy text of the printing and typesetting industry. Lorem Ipsum has been the industry's standard dummy text ever since the 1500 and typesetting industry.</p>
    <div class="more">more...</div>
  </article>

  <h2 class="abs section-title" style="top:1838px"><span>Press Releases</span></h2>

  <article class="abs press" style="left:53px;top:1945px">
    <div class="thumb tone-tower" role="img" aria-label="Glass office tower seen from below"></div>
    <h4>Press Release One</h4>
    <p>Lorem Ipsum is simply dummy text of the printing and typesetting industry. Lorem Ipsum has been the industry's standard dummy text ever since the 1500 and typesetting industry.</p>
  </article>
  <article class="abs press" style="left:595px;top:1945px">
    <div class="thumb tone-meeting" role="img" aria-label="Business people talking at a meeting table"></div>
    <h4>Press Release Two</h4>
    <p>Lorem Ipsum is simply dummy text of the printing and typesetting industry. Lorem Ipsum has been the industry's standard dummy text ever since the 1500 and typesetting industry.</p>
  </article>

  <footer class="abs footer">
    <div class="abs footer-side"></div>
    <div class="abs footer-brand"><span class="brand-dot"></span><span class="brand-name">VELI</span></div>
    <div class="abs fcol" style="left:225px;top:40px">
      <h5>Who We Are</h5>
      <ul><li>About Us</li><li>People</li><li>Press Releases</li><li>Our Mission</li><li>Contact Us</li></ul>
    </div>
    <div class="abs fcol" style="left:395px;top:40px">
      <h5>What We Do</h5>
      <ul><li>Corporate Communications</li><li>Digitilization &amp; Technology Integration</li><li>CSR &amp; Sponsorships</li><li>Investor Relations &amp; Financial PR</li><li>Strategic Transactions</li><li>Corporate Governance</li></ul>
    </div>
    <div class="abs fcol" style="left:650px;top:40px">
      <h5>Insights</h5>
      <ul><li>Intellectual Property</li><li>Social Communities</li><li>Conversations</li></ul>
    </div>
    <div class="abs subscribe">
      <h5>Subscribe News Letter</h5>
      <div class="sub-form"><div class="sub-input">Email</div><div class="sub-btn">Subscribe</div></div>
      <div class="socials" aria-label="Social links"><span></span><span></span><span></span><span></span><span></span></div>
    </div>
    <div class="abs footer-rule"></div>
    <div class="abs copyright">Copyright © 2014 VELI Partners All rights reserved.</div>
    <div class="abs legal"><span>Sitemap</span><span>Privacy Policy</span><span>Terms of Service</span></div>
  </footer>

</div>
</body>
</html>
```